Tobias Wrenfeld and Co stationary design

Name of business:
Tobias Wrenfeld and Co

Can be written as:
Tobias Wrenfeld and Co
Tobias Wrenfeld & Co
tobias wrenfeld & co

If broken into letters:
TW&Co
tw&co

We are a Railway Safety Training Company
Our focus is on rail safety, Rail Management, Safety Management, Train Control Training, Accident Investigation.

.

Project Deadline Extended Reason: The original date was set to commence as soon as the logo contest finished. Sketch guild started the project as soon as it was paid. Added Thursday, May 12, 2016

Target Market(s)

Professionals, CEO's and Managing Directors

Industry/Entity Type

Management Consulting

Font styles to use
Sans Serif

Requirements
Must have
• Professional, Sharp, Creative and modern
• Please note that this is for stationary concept which must include
• - business card
• - letterhead
• - envelope
• - with compliments slip
• - document cover (like book or folder cover)
• - dividers for folders....
• These must all have a common theme or style
Nice to have
• Keep if fresh
Should not have
• Please don't sent just fonts.... Must be creative

```html
<!DOCTYPE html>
<html lang="en">
<head>
<meta charset="utf-8">
<title>Tobias Wrenfeld &amp; Co — Stationery</title>
<link href="https://fonts.googleapis.com/css2?family=Exo+2:ital,wght@0,400;0,700;1,700&family=Montserrat:wght@400;500&display=swap" rel="stylesheet">
<style>
:root{
  --blue:#06418c;
  --orange:#f9a62b;
  --facet:#e4e4e4;
  --facet-dark:#d6d6d6;
  --paper:#ffffff;
  --stage:#ececec;
  --ink:#2a2a2a;
}
*{margin:0;padding:0;box-sizing:border-box}
html,body{width:800px;height:1200px;overflow:hidden;background:var(--stage)}
.canvas{position:relative;width:800px;height:1200px}
.piece{position:absolute;background:var(--paper);overflow:hidden;box-shadow:0 2px 6px rgba(0,0,0,.25)}
.facets{position:absolute;inset:0;width:100%;height:100%}
.brand{font-family:"Exo 2",sans-serif;font-weight:700;color:var(--blue);white-space:nowrap}
.brand-mark{display:inline-block;border-radius:50%;background:var(--orange);vertical-align:middle}
.small-print{font-family:Montserrat,sans-serif;position:absolute;white-space:nowrap;line-height:1.35}
.tab{position:absolute;background:var(--orange)}

/* folder */
.folder-tab-left{left:26px;top:48px;width:324px;height:46px;clip-path:polygon(0 100%,100% 0,100% 100%)}
.folder-tab-right{left:455px;top:48px;width:327px;height:46px;clip-path:polygon(0 0,100% 100%,0 100%)}
.folder-front{left:20px;top:92px;width:362px;height:482px}
.folder-front .brand{position:absolute;left:0;right:0;top:150px;text-align:center;font-size:25px}
.folder-front .brand-mark{width:70px;height:70px;position:absolute;left:146px;top:48px;background:none;border:6px solid var(--blue)}
.folder-front .tagline{position:absolute;left:0;right:0;top:478px;text-align:center;font-family:"Exo 2",sans-serif;font-style:italic;font-weight:700;font-size:12.5px;color:#fff;top:446px;letter-spacing:.3px}
.folder-back{left:421px;top:92px;width:361px;height:482px}
.folder-back .lockup{position:absolute;left:26px;top:400px;display:flex;align-items:center;gap:8px}
.folder-back .brand{color:#fff;font-size:14px}
.folder-back .brand-mark{width:30px;height:30px}
.folder-back .small-print{left:26px;top:446px;font-size:5.6px;color:#fff}

/* letterhead */
.letterhead{left:38px;top:612px;width:342px;height:441px}
.letterhead .lockup{position:absolute;left:28px;top:20px;display:flex;flex-direction:column;align-items:center;gap:5px}
.letterhead .brand-mark{width:22px;height:22px}
.letterhead .brand{font-size:7px}
.letterhead .small-print{left:0;right:0;top:414px;text-align:center;font-size:5.8px;color:var(--ink)}

/* envelope */
.envelope{left:402px;top:612px;width:380px;height:164px}
.envelope .flap-brand{position:absolute;left:0;right:0;top:26px;text-align:center;color:#fff;font-size:10px}

/* compliments slip */
.slip{left:402px;top:790px;width:380px;height:164px}
.slip .lockup{position:absolute;left:20px;top:24px;display:flex;align-items:center;gap:8px}
.slip .brand-mark{width:34px;height:34px}
.slip .brand{font-size:14px}
.slip .small-print{left:0;right:0;top:138px;text-align:center;font-size:5.4px;color:var(--ink)}

/* business card */
.card-front{left:402px;top:965px;width:140px;height:80px}
.card-front .lockup{position:absolute;left:5px;top:10px;display:flex;align-items:center;gap:4px}
.card-front .brand-mark{width:16px;height:16px}
.card-front .brand{font-size:7px}
.card-front .holder{position:absolute;left:82px;top:26px;width:54px;height:6px;background:var(--blue);color:#fff;font-family:Montserrat,sans-serif;font-size:3.4px;text-align:center;line-height:6px}
.card-front .role{position:absolute;left:82px;top:33px;width:54px;text-align:center;font-family:Montserrat,sans-serif;font-size:2px;color:var(--ink)}
.card-front .contact{position:absolute;left:82px;font-family:Montserrat,sans-serif;font-size:2.4px;color:var(--ink);display:flex;gap:3px;align-items:center}
.card-front .contact i{display:inline-block;width:3px;height:3px;border-radius:50%;background:var(--orange)}
.card-back{left:400px;top:1068px;width:142px;height:82px;background:var(--blue)}
.card-back .brand{position:absolute;right:10px;top:10px;color:#fff;font-size:6.5px}
.card-back .tagline{position:absolute;left:10px;top:70px;font-family:"Exo 2",sans-serif;font-style:italic;font-weight:700;font-size:3px;color:#fff}

/* name badge */
.badge{left:648px;top:1040px;width:116px;height:146px;border-radius:6px}
.badge .top{position:absolute;left:8px;top:8px;right:8px;height:112px}
.badge .lockup{position:absolute;left:0;right:0;top:6px;display:flex;flex-direction:column;align-items:center;gap:3px}
.badge .brand-mark{width:12px;height:12px}
.badge .brand{font-size:4px;color:#fff}
.badge .photo{position:absolute;left:34px;top:32px;width:32px;height:32px;background:linear-gradient(160deg,#7c7a76,#c9bfae)}
.badge .holder{position:absolute;left:0;right:0;top:70px;text-align:center;font-family:Montserrat,sans-serif;font-size:4.2px;color:var(--ink)}
.badge .strip{position:absolute;left:0;right:0;top:88px;height:9px;background:var(--orange);color:#fff;text-align:center;font-family:"Exo 2",sans-serif;font-weight:700;font-size:4.4px;line-height:9px}
</style>
</head>
<body>
<main class="canvas">

  <!-- document folder: cover -->
  <div class="tab folder-tab-left"></div>
  <section class="piece folder-front">
    <svg class="facets" viewBox="0 0 453 603" preserveAspectRatio="none" aria-hidden="true">
      <polygon points="0,520 250,505 453,345 453,420 300,390" fill="var(--facet)"/>
      <polygon points="250,505 400,440 453,340 453,290 330,380" fill="#eeeeee"/>
      <polygon points="0,420 0,560 120,520" fill="var(--facet-dark)" opacity=".7"/>
      <polygon points="0,550 125,507 225,390 375,325 453,350 453,603 0,603" fill="var(--blue)"/>
    </svg>
    <span class="brand-mark"></span>
    <div class="brand">Tobias Wrenfeld &amp; Co</div>
    <p class="tagline">(TRAINING AND DEVELOPMENT CONSULTANT)</p>
  </section>

  <!-- document folder: back -->
  <div class="tab folder-tab-right"></div>
  <section class="piece folder-back">
    <svg class="facets" viewBox="0 0 451 603" preserveAspectRatio="none" aria-hidden="true">
      <polygon points="0,230 0,350 90,330" fill="var(--facet)"/>
      <polygon points="200,380 451,420 451,520 330,470" fill="var(--facet)"/>
      <polygon points="380,480 451,430 451,560" fill="var(--facet-dark)" opacity=".7"/>
      <polygon points="0,350 76,325 223,390 323,505 451,550 451,603 0,603" fill="var(--blue)"/>
    </svg>
    <div class="lockup"><span class="brand-mark"></span><span class="brand">TW &amp; Co</span></div>
    <p class="small-print">Tobias Wrenfeld &amp; Co | Lorem ipsum dolor sit amet. Lindvale, Westmark<br>Phone: (xxx) xxx-xxxx &nbsp;| tobias.wrenfeld@railmailbox.net</p>
  </section>

  <!-- letterhead -->
  <section class="piece letterhead">
    <svg class="facets" viewBox="0 0 427 550" preserveAspectRatio="none" aria-hidden="true">
      <polygon points="210,60 427,0 427,90 300,120" fill="var(--facet)"/>
      <polygon points="0,140 210,60 120,150 0,170" fill="#eeeeee"/>
      <polygon points="0,140 70,210 0,280" fill="var(--facet-dark)" opacity=".7"/>
      <polygon points="0,190 160,150 40,300" fill="var(--facet)" opacity=".6"/>
    </svg>
    <div class="lockup"><span class="brand-mark"></span><span class="brand">Tobias Wrenfeld &amp; Co</span></div>
    <p class="small-print">Tobias Wrenfeld &amp; Co | Lorem ipsum dolor sit amet. Lindvale, Westmark<br>Phone: (xxx) xxx-xxxx &nbsp;| tobias.wrenfeld@railmailbox.net</p>
  </section>

  <!-- envelope -->
  <section class="piece envelope">
    <svg class="facets" viewBox="0 0 476 205" preserveAspectRatio="none" aria-hidden="true">
      <polygon points="160,150 300,90 360,200 220,205" fill="var(--facet)"/>
      <polygon points="300,90 476,130 476,205 360,200" fill="#eeeeee"/>
      <path d="M0,0 H476 L466,65 Q462,80 446,80 H30 Q14,80 10,65 Z" fill="var(--blue)"/>
    </svg>
    <div class="brand flap-brand">Tobias Wrenfeld &amp; Co</div>
  </section>

  <!-- compliments slip -->
  <section class="piece slip">
    <svg class="facets" viewBox="0 0 476 207" preserveAspectRatio="none" aria-hidden="true">
      <polygon points="200,90 476,0 476,120 330,80" fill="var(--facet)"/>
      <polygon points="30,207 100,160 130,207" fill="var(--facet-dark)" opacity=".7"/>
      <polygon points="100,160 260,130 330,207 130,207" fill="#eeeeee"/>
      <polygon points="330,80 476,120 476,207 330,207" fill="#f1f1f1"/>
    </svg>
    <div class="lockup"><span class="brand-mark"></span><span class="brand">TW &amp; Co</span></div>
    <p class="small-print">Tobias Wrenfeld &amp; Co | Lorem ipsum dolor sit amet. Lindvale, Westmark<br>Phone: (xxx) xxx-xxxx &nbsp;| tobias.wrenfeld@railmailbox.net | www.tobiaswrenfeld.net</p>
  </section>

  <!-- business card: front -->
  <section class="piece card-front">
    <svg class="facets" viewBox="0 0 176 100" preserveAspectRatio="none" aria-hidden="true">
      <polygon points="0,60 60,45 100,100 0,100" fill="var(--facet)"/>
      <polygon points="80,20 176,0 176,30" fill="#eeeeee"/>
    </svg>
    <div class="lockup"><span class="brand-mark"></span><span class="brand">TW &amp; Co</span></div>
    <div class="holder">Tobias Wrenfeld</div>
    <div class="role">(TRAINING AND DEVELOPMENT CONSULTANT)</div>
    <div class="contact" style="top:42px"><i></i>Lorem ipsum dolor sit amet.<br>Lindvale, Westmark</div>
    <div class="contact" style="top:53px"><i></i>tobias.wrenfeld@railmailbox.net</div>
    <div class="contact" style="top:64px"><i></i>(xxx) xxx-xxxx</div>
  </section>

  <!-- business card: back -->
  <section class="piece card-back">
    <svg class="facets" viewBox="0 0 178 102" preserveAspectRatio="none" aria-hidden="true">
      <polygon points="0,0 30,0 60,40 20,60 0,30" fill="#ffffff"/>
      <polygon points="20,60 60,40 90,55 70,75" fill="var(--facet)"/>
      <polygon points="120,75 178,60 178,102 150,102" fill="#ffffff"/>
      <polygon points="90,55 150,70 120,80" fill="var(--facet)" opacity=".8"/>
    </svg>
    <div class="brand">Tobias Wrenfeld &amp; Co</div>
    <p class="tagline">(TRAINING AND DEVELOPMENT CONSULTANT)</p>
  </section>

  <!-- name badge -->
  <section class="piece badge">
    <div class="top">
      <svg class="facets" viewBox="0 0 100 112" preserveAspectRatio="none" aria-hidden="true">
        <polygon points="0,0 100,0 100,70 0,80" fill="var(--blue)"/>
        <polygon points="0,60 40,75 0,80" fill="var(--facet)"/>
      </svg>
      <div class="lockup"><span class="brand-mark"></span><span class="brand">Tobias Wrenfeld &amp; Co</span></div>
      <div class="photo" role="img" aria-label="Staff portrait photo"></div>
      <p class="holder">Tobias Wrenfeld<br>(Training and Development Consultant)</p>
      <div class="strip">OFFICIAL MANAGEMENT</div>
    </div>
  </section>

</main>
</body>
</html>
```